Telecommunications/Power civil contractor needs business card design

Were a new telecommunications/power underground civil contractor that is looking for a new business card design. Our company colours are silver or grey and orange. Feel free to use the white background logo or the black background logo.

Target Market(s)

Local contractors, utility companies, private sector mining/energy companies, developers.

Industry/Entity Type

Telecommunications

Contact Information for Business Card

Each card will need the following info:
Persons name:
Title:
E-mail:
Phone number:
Shop Address:
Mailing Address:

Requirements
Must have
• Each card will need the following info:
• Persons name:
• Title:
• E-mail:
• Phone number:
• Shop Address:
• Mailing Address:

```html
<!DOCTYPE html>
<html lang="en">
<head>
<meta charset="utf-8">
<title>Ridgeline Civil Inc – Business Card</title>
<link rel="stylesheet" href="https://fonts.googleapis.com/css2?family=Open+Sans:wght@400;700&display=swap">
<style>
  :root {
    --orange: #f05a28;
    --grey: #6d6e71;
    --silver: #9a9b9e;
    --white: #ffffff;
    --black: #0b0b0b;
    --backdrop: #2b2b2b;
  }
  * { box-sizing: border-box; margin: 0; padding: 0; }
  html, body { width: 1200px; height: 907px; overflow: hidden; }
  body {
    background: var(--backdrop);
    font-family: "Open Sans", Arial, sans-serif;
    position: relative;
  }
  .card {
    position: absolute;
    top: 303px;
    width: 520px;
    height: 300px;
    overflow: hidden;
    box-shadow: 0 10px 26px rgba(0,0,0,.45);
  }
  .card--front { left: 50px; background: var(--orange); }
  .card--back { left: 630px; background: var(--black); }

  .front-panel { position: absolute; inset: 0; }

  .brand {
    position: absolute;
    display: flex;
    align-items: center;
    gap: 10px;
  }
  .brand__mark {
    width: 30px; height: 30px;
    border-radius: 50%;
    background: var(--orange);
    flex: none;
  }
  .brand__name {
    font-weight: 700;
    font-size: 22px;
    letter-spacing: .5px;
    line-height: 1.05;
    text-transform: uppercase;
  }
  .card--front .brand { left: 34px; top: 128px; }
  .card--front .brand__name { color: var(--grey); }
  .card--back .brand { left: 50%; top: 50%; transform: translate(-50%, -50%); }
  .card--back .brand__name { color: var(--silver); }

  .contact {
    position: absolute;
    right: 28px;
    top: 28px;
    text-align: right;
    color: var(--white);
  }
  .contact__name { font-weight: 700; font-size: 17px; text-transform: uppercase; letter-spacing: .3px; }
  .contact__title { font-size: 12px; margin-bottom: 14px; color: #1c1c1c; }
  .contact__line { font-size: 12.5px; line-height: 1.45; }
  .contact__row { display: flex; justify-content: flex-end; align-items: center; gap: 6px; }
  .contact__gap { height: 12px; }
  .icon { width: 12px; height: 12px; flex: none; }
</style>
</head>
<body>
  <section class="card card--front" aria-label="Business card front">
    <svg class="front-panel" width="520" height="300" viewBox="0 0 520 300">
      <polygon points="0,0 150,0 240,90 240,300 0,300" fill="var(--white)"/>
      <polyline points="150,0 240,90 240,300" fill="none" stroke="var(--grey)" stroke-width="4"/>
    </svg>
    <div class="brand">
      <span class="brand__mark"></span>
      <span class="brand__name">Ridgeline<br>Civil Inc</span>
    </div>
    <div class="contact">
      <div class="contact__name">Marlo Thane</div>
      <div class="contact__title">Managing Director</div>
      <div class="contact__row">
        <div>
          <div class="contact__line">N. 4 Quarry Lane,</div>
          <div class="contact__line">Suite 210, Tacoma, WA 98402</div>
        </div>
        <svg class="icon" viewBox="0 0 12 12"><circle cx="6" cy="6" r="6" fill="var(--grey)"/><path d="M6 2.5a2.2 2.2 0 0 0-2.2 2.2C3.8 6.4 6 9.5 6 9.5s2.2-3.1 2.2-4.8A2.2 2.2 0 0 0 6 2.5z" fill="var(--white)"/></svg>
      </div>
      <div class="contact__gap"></div>
      <div class="contact__row">
        <span class="contact__line">555.014.272</span>
        <svg class="icon" viewBox="0 0 12 12"><circle cx="6" cy="6" r="6" fill="var(--grey)"/><path d="M4 3l1.2 1.6-.7.8c.5 1 1.1 1.6 2.1 2.1l.8-.7L9 8l-.6 1.1C6 9 3.1 6 3 3.6z" fill="var(--white)"/></svg>
      </div>
      <div class="contact__row">
        <span class="contact__line">info@ridgelinecivil.com</span>
        <svg class="icon" viewBox="0 0 12 12"><circle cx="6" cy="6" r="6" fill="var(--grey)"/><rect x="3" y="4" width="6" height="4.2" fill="var(--white)"/><path d="M3 4l3 2.3L9 4" fill="none" stroke="var(--grey)" stroke-width=".7"/></svg>
      </div>
    </div>
  </section>

  <section class="card card--back" aria-label="Business card back">
    <div class="brand">
      <span class="brand__mark"></span>
      <span class="brand__name">Ridgeline<br>Civil Inc</span>
    </div>
  </section>
</body>
</html>
```